Grand Opening Celebration of Radiant Glow Atelier

We need a flyer designer for a new eyelash and skincare studio that just opened in Aliso Viejo, CA. We specialize in Eyelash enhancement artistry, and perform various services such as vegan/organic spray tans, full body waxing, makeup artistry and customized facials. We are having a Grand opening celebration to make the community aware that we are here, to drum up business and to have locals attend the opening. So I need a flyer that will give the info for that and be appealing to both men and women, as I start to figure out the vendors that will be there I will send their info. SO I would like to just see a couple rough drafts to see if you can do the style I am looking for. My inspirations are vellora, mirel, tox, dean harlow, companies like that. My website is this www.radiantglowatelier.com

Event will be on December 6 at 3:00. 48 Corbel Lane, Aliso Viejo, CA 92601

```html
<!DOCTYPE html>
<html lang="en">
<head>
<meta charset="utf-8">
<title>Grand Opening – Radiant Glow Atelier</title>
<link rel="stylesheet" href="https://fonts.googleapis.com/css2?family=Arimo:wght@400;700&family=Josefin+Sans:wght@100&display=swap">
<style>
  :root {
    --paper: #ffffff;
    --ink: #111111;
    --muted: #6b6b6b;
    --display-grey: #b9b9b9;
    --accent: #e0574a;
    --photo-brick: #9a5a48;
    --photo-light: #e6ddd6;
  }
  html, body {
    margin: 0;
    padding: 0;
    overflow: hidden;
    background: var(--paper);
  }
  .flyer {
    position: relative;
    width: 848px;
    height: 1200px;
    overflow: hidden;
    background: var(--paper);
    font-family: "Arimo", Arial, sans-serif;
    color: var(--ink);
  }
  .hero-photo {
    position: absolute;
    left: 228px;
    top: 0;
    width: 409px;
    height: 313px;
    background: linear-gradient(160deg, var(--photo-brick) 0%, #b77a64 45%, var(--photo-light) 100%);
  }
  .hero-photo-base {
    position: absolute;
    left: 212px;
    top: 313px;
    width: 445px;
    height: 98px;
    background: linear-gradient(180deg, #e9e2dc 0%, #f6f2ef 100%);
    border-radius: 40px 40px 0 0;
  }
  .divider {
    position: absolute;
    left: 133px;
    top: 411px;
    width: 582px;
    height: 3px;
    background: var(--accent);
  }
  .event-info {
    position: absolute;
    left: 0;
    top: 420px;
    width: 848px;
    text-align: center;
    line-height: 1.05;
  }
  .event-date {
    margin: 0;
    font-size: 31px;
    font-weight: 700;
    letter-spacing: -0.3px;
  }
  .event-date .event-time {
    font-size: 17px;
    font-weight: 400;
  }
  .event-street {
    margin: 2px 0 0;
    font-size: 44px;
    font-weight: 400;
    letter-spacing: 0.3px;
  }
  .event-city {
    margin: 4px 0 0;
    font-size: 29px;
    font-weight: 400;
    letter-spacing: 0.5px;
  }
  .headline {
    position: absolute;
    left: 0;
    top: 620px;
    width: 848px;
    margin: 0;
    font-family: "Josefin Sans", "Helvetica Neue", sans-serif;
    font-weight: 100;
    color: var(--display-grey);
    line-height: 1;
  }
  .headline-word {
    position: absolute;
    white-space: nowrap;
    letter-spacing: -6px;
  }
  .headline-grand {
    left: 160px;
    top: 0;
    font-size: 230px;
  }
  .headline-opening {
    left: 28px;
    top: 150px;
    font-size: 236px;
  }
  .headline-dot {
    position: absolute;
    left: 562px;
    top: 800px;
    width: 16px;
    height: 16px;
    border-radius: 50%;
    background: var(--accent);
  }
  .services {
    position: absolute;
    left: 152px;
    top: 1062px;
    width: 340px;
    margin: 0;
    font-size: 11px;
    line-height: 1.45;
    color: var(--muted);
    text-align: justify;
  }
  .brand {
    position: absolute;
    left: 570px;
    top: 1040px;
    width: 250px;
    display: flex;
    align-items: center;
    gap: 10px;
  }
  .brand-mark {
    flex: none;
    width: 18px;
    height: 18px;
    border-radius: 50%;
    background: var(--ink);
  }
  .brand-name {
    font-size: 23px;
    font-weight: 700;
    line-height: 1.1;
    color: var(--ink);
    text-transform: uppercase;
  }
  .web-band {
    position: absolute;
    left: 185px;
    top: 1140px;
    width: 663px;
    height: 60px;
    background: linear-gradient(90deg, rgba(224, 87, 74, 0) 0%, rgba(224, 87, 74, 0.55) 35%, var(--accent) 70%);
  }
  .web-address {
    position: absolute;
    right: 24px;
    top: 1155px;
    margin: 0;
    font-size: 21px;
    font-weight: 700;
    color: var(--ink);
  }
</style>
</head>
<body>
  <main class="flyer">
    <div class="hero-photo" role="img" aria-label="Photo of a smiling woman with long dark curly hair sitting cross-legged in front of a red brick wall"></div>
    <div class="hero-photo-base" role="img" aria-label="Lower part of the photo showing the woman's crossed legs"></div>

    <div class="divider"></div>

    <section class="event-info">
      <p class="event-date">December 6 <span class="event-time">at 3:00.</span></p>
      <p class="event-street">48 Corbel Lane,</p>
      <p class="event-city">Aliso Viejo, CA 92601</p>
    </section>

    <h1 class="headline">
      <span class="headline-word headline-grand">Grand</span>
      <span class="headline-word headline-opening">Opening</span>
    </h1>
    <div class="headline-dot"></div>

    <p class="services">Specialize in Eyelash enhancement artistry, and perform various services such as vegan/organic spray tans, full body waxing, makeup artistry and customized facials.</p>

    <div class="brand">
      <span class="brand-mark"></span>
      <span class="brand-name">Radiant Glow Atelier</span>
    </div>

    <div class="web-band"></div>
    <p class="web-address">www.radiantglowatelier.com</p>
  </main>
</body>
</html>
```